Business Card For Video Production Company

Please NOTE: I've added some info to the must haves that I should have included at the start. Thank you.

I need a business card design for my video production company based in Orlando called Halvard Lens Productions. Our work consists of web video marketing (web videos), training videos, sales videos, conference and seminar video production...basically a lot of corporate based work.

We work with successful small businesses, not-for-profits and some Summit 700 type groups. We bring a lot of knowledge, experience and attention to detail to every project.

I'd like something that communicates strength, confidence, integrity, as well as creative vision. I want to stay away from the standard icons of the media and film industry. I'd like to emphasize the colors of my logo, and also the colors of my website which has a white background. Simple is good.

Our budgets are moderate...generally $1500 to $5000.

www.halvardlens.tv

PS...We don't do weddings or recitals, or that type of production.
Updates

I want to thank all the designers for your updates. There's way too many to be able to give feedback on for all. I hope you understand that. But wow…there are so many great designs everyone has offered. I can't thank you enough…each and everyone. I hope to make my decision soon. I'm not accepting anymore designs from new designers. Dean-

Target Market(s)

Successful small businesses, marketing directors, corporate communication directors, training and human resources professionals. forward thinking not-for profits. Since my company is based in Central Florida, most of my work comes from this area too.

Industry/Entity Type

Marketing

Requirements
Must have
• website address, www.halvardlens.tv
phone number, 407-555-2937
email address, dean@halvardlens.tv

Title
Dean Halvard
Owner/Creative Director

I'd like to have a single line that goes across illustrating our services, maybe separated with bullet points:

Marketing Videos, Corporate Videos, Conference & Seminar Video Production
Should not have
• No film or video icons.
No need to pull language or copy from my website.

```html
<!DOCTYPE html>
<html lang="en">
<head>
<meta charset="UTF-8">
<title>Halvard Lens Productions — Business Card</title>
<link href="https://fonts.googleapis.com/css2?family=Montserrat:wght@300;400;600;800&display=swap" rel="stylesheet">
<style>
  :root{
    --navy:#0a3c84;
    --ocean:#0b6fb8;
    --sky:#0d9bd6;
    --stripe-mid:#1590e2;
    --stripe-light:#8fd4f8;
    --cyan-title:#22a7e8;
    --ink:#3a3a3a;
    --paper:#ffffff;
    --backdrop:#eef1f5;
  }
  *{box-sizing:border-box;margin:0;padding:0}
  html,body{width:1200px;height:873px;overflow:hidden}
  body{background:var(--backdrop);font-family:"Montserrat",sans-serif;position:relative}
  .card{position:absolute;top:121px;width:360px;height:630px;background:var(--paper);
        overflow:hidden;box-shadow:0 10px 30px rgba(10,40,90,.18)}
  .card--front{left:200px}
  .card--back{left:640px}
  .card__art{position:absolute;inset:0}

  /* front */
  .front__contact{position:absolute;left:0;right:0;top:24px;transform:rotate(180deg);
        transform-origin:center 50px;color:var(--stripe-mid);font-size:15px;line-height:1.6;
        padding-left:70px;height:100px;display:flex;flex-direction:column;justify-content:flex-end}
  .front__contact li{list-style:none;display:flex;align-items:center;gap:8px}
  .front__contact svg{width:11px;height:11px;fill:var(--stripe-mid)}
  .front__brand{position:absolute;left:180px;top:420px;transform:translate(-50%,-50%) rotate(90deg);
        display:flex;align-items:center;gap:14px;white-space:nowrap}
  .brand-mark{width:40px;height:40px;background:currentColor;flex:none}
  .front__brand{color:var(--paper)}
  .brand-name{font-weight:800;font-size:26px;letter-spacing:.2px}

  /* back */
  .back__info{position:absolute;left:40px;right:30px;top:44px;color:var(--paper)}
  .back__name{color:var(--cyan-title);font-weight:800;font-size:34px;line-height:.95;text-transform:uppercase}
  .back__roles{font-weight:300;color:var(--cyan-title);font-size:22px;line-height:1.1;margin-top:4px}
  .back__roles li{list-style:none}
  .back__roles li:first-child{padding-left:40px}
  .back__services{color:var(--cyan-title);font-weight:400;font-size:13px;line-height:1.35;margin-top:26px}
  .back__contact{list-style:none;text-align:center;margin-top:26px;font-size:15px;line-height:1.3}
  .back__contact li{margin-bottom:12px;display:flex;flex-direction:column;align-items:center;gap:3px}
  .back__contact svg{width:12px;height:12px;fill:var(--paper)}
  .back__brand{position:absolute;left:34px;bottom:50px;display:flex;align-items:center;gap:12px;color:var(--ink)}
  .back__brand .brand-mark{background:var(--stripe-mid);width:34px;height:34px}
  .back__brand .brand-name{font-size:22px}
</style>
</head>
<body>

<section class="card card--front" aria-label="Card front">
  <svg class="card__art" viewBox="0 0 360 630" aria-hidden="true">
    <defs>
      <linearGradient id="frontBlue" x1="0" y1="0" x2="0.3" y2="1">
        <stop offset="0" stop-color="#0aa6d8"/>
        <stop offset="0.45" stop-color="#0b6fb8"/>
        <stop offset="1" stop-color="#0a3c84"/>
      </linearGradient>
    </defs>
    <polygon points="0,236 144,156 360,236 360,630 0,630" fill="var(--stripe-light)"/>
    <polygon points="0,252 144,172 360,252 360,630 0,630" fill="var(--stripe-mid)"/>
    <polygon points="0,268 144,188 360,268 360,630 0,630" fill="url(#frontBlue)"/>
  </svg>
  <ul class="front__contact">
    <li><svg viewBox="0 0 10 10"><circle cx="5" cy="5" r="4"/></svg>: halvardlens.tv</li>
    <li><svg viewBox="0 0 10 10"><path d="M0 2h10v6H0z"/></svg>: dean@halvardlens.tv</li>
    <li><svg viewBox="0 0 10 10"><path d="M2 0h3l1 3-2 1a6 6 0 0 0 2 2l1-2 3 1v3l-2 2C4 10 0 6 0 2z"/></svg>: 407-555-2937</li>
  </ul>
  <div class="front__brand">
    <span class="brand-mark"></span>
    <span class="brand-name">Halvard Lens Productions</span>
  </div>
</section>

<section class="card card--back" aria-label="Card back">
  <svg class="card__art" viewBox="0 0 360 630" aria-hidden="true">
    <defs>
      <linearGradient id="backBlue" x1="0" y1="0" x2="0.2" y2="1">
        <stop offset="0" stop-color="#0a3c84"/>
        <stop offset="0.55" stop-color="#0b5fa8"/>
        <stop offset="1" stop-color="#0aa6d8"/>
      </linearGradient>
    </defs>
    <polygon points="0,0 360,0 360,398 216,478 0,398" fill="var(--stripe-light)"/>
    <polygon points="0,0 360,0 360,382 216,462 0,382" fill="var(--stripe-mid)"/>
    <polygon points="0,0 360,0 360,366 216,446 0,366" fill="url(#backBlue)"/>
  </svg>
  <div class="back__info">
    <h1 class="back__name">Dean<br>Halvard</h1>
    <ul class="back__roles">
      <li>• Owner</li>
      <li>• Creative Director</li>
    </ul>
    <p class="back__services">• Marketing Videos • Corporate Videos<br>• Conference &amp; Seminar Video</p>
    <ul class="back__contact">
      <li><svg viewBox="0 0 10 10"><circle cx="5" cy="5" r="4"/></svg>halvardlens.tv</li>
      <li><svg viewBox="0 0 10 10"><path d="M0 2h10v6H0z"/></svg>dean@halvardlens.tv</li>
      <li><svg viewBox="0 0 10 10"><path d="M2 0h3l1 3-2 1a6 6 0 0 0 2 2l1-2 3 1v3l-2 2C4 10 0 6 0 2z"/></svg>407-555-2937</li>
    </ul>
  </div>
  <div class="back__brand">
    <span class="brand-mark"></span>
    <span class="brand-name">Halvard Lens Productions</span>
  </div>
</section>

</body>
</html>
```